Packaging Design New Cosmetics Range

Small Establish online Beauty company is expanding it's product range into Serums, Sprays and Creams . We are looking for a new fresh packaging design for this launch.
We only use products that are Organic , Not Tested on Animals and Natural products
We would be interested in viewing a White Design , Black design and a designer choice of colors .
First Products are
Rose Water in 100ml glass bottle with box
and a set of 3 Face Serums Vit C , Retinol and Hyaluronic in 30ml Glass bottle = Box
Scrubs and creams will launch later in Q1 2020 however would like a similar feel across all products
Target Market(s)
SEA / US Markets
Industry/Entity Type
Cosmetics
Colors
Designer to choose colors to be used in the design.
Requirements
Must have
- Space Allocated for Product Use and Bar Codes on Box
Nice to have
- Organic , Not tested on animal Logo's

```html
<!DOCTYPE html>
<html lang="en">
<head>
<meta charset="utf-8">
<title>Solvane Rose Water – Packaging Fronts</title>
<link rel="stylesheet" href="https://fonts.googleapis.com/css2?family=Barlow:wght@300;400&family=Open+Sans:wght@400&display=swap">
<style>
  :root {
    --page: #ffffff;
    --teal: #1fa88f;
    --ink: #111111;
    --paper: #ffffff;
    --night: #000000;
    --ornament-light: #d9d9d9;
    --ornament-dark: #6a6a6a;
    --tagline-light: #3a3a3a;
    --tagline-dark: #d8d8d8;
  }
  * { box-sizing: border-box; margin: 0; padding: 0; }
  html, body {
    width: 1200px;
    height: 600px;
    overflow: hidden;
    background: var(--page);
  }
  .range {
    width: 1200px;
    height: 600px;
    display: flex;
    justify-content: center;
    align-items: center;
    gap: 60px;
  }
  .pack-front {
    position: relative;
    width: 320px;
    height: 480px;
    overflow: hidden;
    box-shadow: 2px 3px 6px rgba(0,0,0,0.18);
    text-align: center;
  }
  .pack-front--white { background: var(--paper); }
  .pack-front--black { background: var(--night); }

  .ornament {
    position: absolute;
    left: 50%;
    width: 250px;
    height: 125px;
    transform: translateX(-50%);
  }
  .ornament--top {
    top: -10px;
    border-radius: 0 0 125px 125px;
  }
  .ornament--bottom {
    bottom: -10px;
    border-radius: 125px 125px 0 0;
  }
  .pack-front--white .ornament--top {
    background: radial-gradient(ellipse at 50% 0%, var(--ornament-light) 0%, #e8e8e8 60%, rgba(232,232,232,0) 100%);
  }
  .pack-front--white .ornament--bottom {
    background: radial-gradient(ellipse at 50% 100%, var(--ornament-light) 0%, #e8e8e8 60%, rgba(232,232,232,0) 100%);
  }
  .pack-front--black .ornament--top {
    background: radial-gradient(ellipse at 50% 0%, var(--ornament-dark) 0%, #4a4a4a 60%, rgba(74,74,74,0) 100%);
  }
  .pack-front--black .ornament--bottom {
    background: radial-gradient(ellipse at 50% 100%, var(--ornament-dark) 0%, #4a4a4a 60%, rgba(74,74,74,0) 100%);
  }

  .brand-name {
    position: absolute;
    top: 190px;
    left: 0;
    right: 0;
    font-family: "Barlow", sans-serif;
    font-weight: 300;
    font-size: 50px;
    line-height: 1;
    color: var(--teal);
  }
  .product-name {
    position: absolute;
    top: 283px;
    left: 0;
    right: 0;
    font-family: "Open Sans", sans-serif;
    font-weight: 400;
    font-size: 20px;
    letter-spacing: 1px;
  }
  .pack-front--white .product-name { color: var(--ink); }
  .pack-front--black .product-name { color: #ffffff; }
  .claims {
    position: absolute;
    top: 330px;
    left: 0;
    right: 0;
    font-family: "Barlow", sans-serif;
    font-weight: 300;
    font-size: 16px;
    letter-spacing: 3px;
  }
  .pack-front--white .claims { color: var(--tagline-light); }
  .pack-front--black .claims { color: var(--tagline-dark); }
</style>
</head>
<body>
  <main class="range">
    <section class="pack-front pack-front--white">
      <div class="ornament ornament--top" role="img" aria-label="Light grey mandala ornament bleeding off the top edge"></div>
      <p class="brand-name">Solvane</p>
      <p class="product-name">rose water</p>
      <p class="claims">organic | cruelty-free</p>
      <div class="ornament ornament--bottom" role="img" aria-label="Light grey mandala ornament bleeding off the bottom edge"></div>
    </section>

    <section class="pack-front pack-front--black">
      <div class="ornament ornament--top" role="img" aria-label="Dark grey mandala ornament bleeding off the top edge"></div>
      <p class="brand-name">Solvane</p>
      <p class="product-name">rose water</p>
      <p class="claims">organic | cruelty-free</p>
      <div class="ornament ornament--bottom" role="img" aria-label="Dark grey mandala ornament bleeding off the bottom edge"></div>
    </section>
  </main>
</body>
</html>
```